Design for Flavored drink product

I need a packaging design for flavoured drinks product.
The product is a flavoured drink product.

There will be various flavours i.e. orange, apple, strawberry, etc.
However, you may design the product using one sample flavour first (i.e. orange), as the designs of other flavours could be adjusted afterwards.

The temporary product name is: ZIBBLO

The measurement is 20,2 cm (Length) x 12,8 cm (Height).

The target customers are young audiences (10 years - 35 years old).

I want the product design to be something 'fun' and 'colourful'.
The design concept could be anything depends on your imagination.
Basically, I want you to be creative in designing the logo and the overall graphic design for the label.

I am hoping to have a product design that can stand out in the supermarket shelf.
It must be eye catchy and attractive.

- Create something different. Something extraordinary -

Note: You may refer to design sample attached

Thank you and Good Luck!

Thank you,
Marcus

```html
<!DOCTYPE html>
<html lang="en">
<head>
<meta charset="utf-8">
<title>Zibblo Strawberry Juice Label</title>
<link rel="stylesheet" href="https://fonts.googleapis.com/css2?family=Chewy&family=Arimo:wght@400;700&family=Special+Elite&display=swap">
<style>
  :root {
    --paper: #ffffff;
    --stripe-a: #ffe81a;
    --stripe-b: #ffdf00;
    --leaf-green: #2e8a1e;
    --berry: #e8325a;
    --berry-soft: #f28bb0;
    --peach: #f7a860;
    --lime: #58e23a;
    --ink: #111111;
  }
  * { box-sizing: border-box; margin: 0; padding: 0; }
  html, body { width: 846px; height: 1200px; overflow: hidden; background: var(--paper); }
  .canvas { position: relative; width: 846px; height: 1200px; }

  .brand-mark {
    position: absolute; left: 0; top: 110px; width: 846px; text-align: center;
    font-family: "Chewy", cursive; font-size: 118px; color: var(--leaf-green); line-height: 1;
  }

  .label {
    position: absolute; left: 35px; top: 474px; width: 811px; height: 514px; overflow: hidden;
    background: repeating-linear-gradient(90deg, var(--stripe-a) 0 12px, var(--stripe-b) 12px 24px);
  }
  .label-art {
    position: absolute; left: 30px; top: 70px; width: 470px; height: 430px;
    border-radius: 48% 52% 40% 50%;
    background: radial-gradient(circle at 45% 45%, var(--berry) 0 28%, var(--berry-soft) 42%, var(--peach) 58%, rgba(247,168,96,0) 72%);
  }
  .label-brand {
    position: absolute; left: 88px; top: 22px;
    font-family: "Chewy", cursive; font-size: 46px; color: var(--leaf-green); line-height: 1;
  }
  .flavour-name {
    position: absolute; left: 100px; top: 175px; width: 380px;
    font-family: "Chewy", cursive; font-size: 70px; line-height: 0.9; color: #fff;
    -webkit-text-stroke: 3px var(--berry); paint-order: stroke fill;
    transform: rotate(-16deg); transform-origin: left top;
  }
  .flavour-name .second-line { display: block; padding-left: 170px; }

  .ingredients-title {
    position: absolute; left: 585px; top: 40px; width: 180px; text-align: center;
    font-family: "Special Elite", monospace; font-weight: 700; font-size: 32px; color: var(--ink); letter-spacing: 1px;
  }
  .facts {
    position: absolute; left: 549px; top: 96px; width: 248px;
    border: 2px solid var(--ink); padding: 2px 5px 3px;
    font-family: "Arimo", Arial, sans-serif; font-size: 12.5px; color: var(--ink); line-height: 17.5px;
  }
  .facts-title { font-weight: 700; font-size: 17px; letter-spacing: 2.4px; line-height: 22px; }
  .facts-serving { font-weight: 700; font-size: 12px; border-bottom: 7px solid var(--ink); padding-bottom: 3px; }
  .facts-row { display: flex; justify-content: space-between; }
  .facts-head { font-weight: 700; text-decoration: underline; margin-top: 2px; }
  .facts-blend { font-weight: 700; border-top: 3px solid var(--ink); border-bottom: 1px solid var(--ink); }
  .facts-row .amt { flex: 1; text-align: right; padding-right: 14px; }
  .facts-list { border-bottom: 7px solid var(--ink); padding-bottom: 1px; }
  .facts-note { font-size: 9.5px; line-height: 14px; }
  .other-ingredients {
    position: absolute; left: 556px; top: 428px;
    font-family: "Arimo", Arial, sans-serif; font-size: 12.5px; color: var(--ink);
  }
</style>
</head>
<body>
<div class="canvas">
  <div class="brand-mark">Zibblo</div>

  <section class="label">
    <div class="label-art" role="img" aria-label="Illustration of a strawberry with juice splashes, leaves and a stick figure character"></div>
    <div class="label-brand">Zibblo</div>
    <h1 class="flavour-name">strawberry<span class="second-line">juice</span></h1>

    <h2 class="ingredients-title">INGREDIENTS</h2>
    <div class="facts">
      <div class="facts-title">Supplement Facts</div>
      <div class="facts-serving">Serving Size: 1 Packet (6.65g)</div>
      <div class="facts-row facts-head"><span>Amount per Packet</span><span>% DV</span></div>
      <div class="facts-row"><span>Vitamin E</span><span class="amt">350mg</span><span>2333 %</span></div>
      <div class="facts-row"><span>Vitamin C</span><span class="amt">60mg</span><span>67 %</span></div>
      <div class="facts-row facts-blend"><span>Proprietary Blend</span><span class="amt">2940mg</span></div>
      <div class="facts-list">
        <div class="facts-row"><span>NAC - Essential Amino Acid</span><span>*</span></div>
        <div class="facts-row"><span>Dandelion Root Extract</span><span>*</span></div>
        <div class="facts-row"><span>Gypsyweed Extract</span><span>*</span></div>
        <div class="facts-row"><span>L-Glutamine</span><span>*</span></div>
        <div class="facts-row"><span>St. Mary Thistle Extract</span><span>*</span></div>
        <div class="facts-row"><span>Asparagus Root Extract</span><span>*</span></div>
        <div class="facts-row"><span>Prickly Pear Extract</span><span>*</span></div>
        <div class="facts-row"><span>European Elder Flower Extract</span><span>*</span></div>
        <div class="facts-row"><span>Lady's Mantel Extract</span><span>*</span></div>
      </div>
      <div class="facts-note">*Daily Value (DV) not established.</div>
    </div>
    <p class="other-ingredients">Other Ingredients: Honey Powder</p>
  </section>
</div>
</body>
</html>
```